Lumindo Business Card

Need a business card for our business.

Attached are our Logos. There is either the white and black all the all red with white. Either Logo can be used.

The winner will be provided the details for phone number and address.

Good Luck!

Business

```html
<!DOCTYPE html>
<html lang="en">
<head>
<meta charset="utf-8">
<title>Lumindo Industries Business Card</title>
<link rel="stylesheet" href="https://fonts.googleapis.com/css2?family=Montserrat:wght@700;800&family=Didact+Gothic&display=swap">
<style>
  :root {
    --bg: #2a2a2a;
    --red: #c0282c;
    --red-dark: #7a1518;
    --red-mid: #a52226;
    --paper: #f7f7f6;
    --ink: #3a3a3a;
    --ink-soft: #555555;
    --rule: #e2e2e2;
  }
  * { margin: 0; padding: 0; box-sizing: border-box; }
  html, body { width: 1200px; height: 900px; overflow: hidden; }
  body {
    background: var(--bg);
    position: relative;
    font-family: "Didact Gothic", sans-serif;
  }
  .card {
    position: absolute;
    left: 250px;
    width: 700px;
    height: 400px;
    border-radius: 3px;
    box-shadow: 0 10px 30px rgba(0,0,0,.45);
  }
  .card-back {
    top: 40px;
    background: radial-gradient(ellipse at 55% 45%, var(--red-mid) 0%, var(--red-dark) 85%);
    display: flex;
    align-items: center;
    justify-content: center;
  }
  .card-front {
    top: 460px;
    background: var(--paper);
  }
  .wordmark {
    font-family: "Montserrat", sans-serif;
    font-weight: 800;
    text-transform: uppercase;
    line-height: 1;
    display: flex;
    flex-direction: column;
    align-items: center;
  }
  .wordmark-main { font-size: 48px; letter-spacing: 1px; }
  .wordmark-sub { font-size: 15px; letter-spacing: 9px; margin-top: 8px; padding-left: 9px; }
  .card-back .wordmark { color: #ffffff; }
  .card-front .wordmark {
    position: absolute;
    left: 40px;
    width: 320px;
    top: 168px;
    color: var(--red);
  }
  .divider {
    position: absolute;
    left: 400px;
    top: 30px;
    bottom: 30px;
    width: 1px;
    background: var(--rule);
  }
  .details {
    position: absolute;
    left: 430px;
    top: 58px;
    color: var(--ink);
  }
  .person-name {
    font-family: "Montserrat", sans-serif;
    font-weight: 700;
    font-size: 21px;
    letter-spacing: .5px;
    text-transform: uppercase;
  }
  .person-title {
    font-size: 16px;
    color: var(--ink-soft);
    margin: 2px 0 22px 14px;
  }
  .contact-list { list-style: none; margin-left: 28px; }
  .contact-item {
    display: flex;
    align-items: center;
    gap: 8px;
    font-size: 16px;
    line-height: 24px;
  }
  .contact-icon { width: 15px; height: 15px; flex: none; }
  .address {
    margin: 28px 0 0 80px;
    font-size: 16px;
    line-height: 24px;
    font-style: normal;
  }
</style>
</head>
<body>
  <section class="card card-back" aria-label="Card back">
    <p class="wordmark"><span class="wordmark-main">Lumindo</span><span class="wordmark-sub">Industries</span></p>
  </section>

  <section class="card card-front" aria-label="Card front">
    <p class="wordmark"><span class="wordmark-main">Lumindo</span><span class="wordmark-sub">Industries</span></p>
    <div class="divider"></div>
    <div class="details">
      <h1 class="person-name">Jordan Hale</h1>
      <p class="person-title">General Manager</p>
      <ul class="contact-list">
        <li class="contact-item">
          <svg class="contact-icon" viewBox="0 0 16 16" aria-hidden="true"><circle cx="8" cy="8" r="7" fill="none" stroke="#c0282c" stroke-width="1.5"/><path d="M5.5 4.5l1.5 0 .6 1.8-1 .8a5 5 0 0 0 2.3 2.3l.8-1 1.8.6v1.5c-3.5.3-6.3-2.5-6-6z" fill="#c0282c"/></svg>
          (555) 014-2210
        </li>
        <li class="contact-item">
          <svg class="contact-icon" viewBox="0 0 16 16" aria-hidden="true"><circle cx="8" cy="8" r="7" fill="none" stroke="#c0282c" stroke-width="1.5"/><rect x="4.5" y="6.5" width="7" height="4.5" fill="#c0282c"/><rect x="5.8" y="4.3" width="4.4" height="2.2" fill="#c0282c"/></svg>
          (555) 014-2211
        </li>
        <li class="contact-item">
          <svg class="contact-icon" viewBox="0 0 16 16" aria-hidden="true"><circle cx="8" cy="8" r="7" fill="none" stroke="#c0282c" stroke-width="1.5"/><rect x="4.3" y="5.3" width="7.4" height="5.4" fill="#c0282c"/><path d="M4.3 5.3l3.7 3 3.7-3" fill="none" stroke="#ffffff" stroke-width="1"/></svg>
          info@lumindoind.com
        </li>
        <li class="contact-item">
          <svg class="contact-icon" viewBox="0 0 16 16" aria-hidden="true"><g fill="none" stroke="#c0282c" stroke-width="1.3"><circle cx="8" cy="8" r="7"/><ellipse cx="8" cy="8" rx="3" ry="7"/><path d="M1 8h14M2.2 4.5h11.6M2.2 11.5h11.6"/></g></svg>
          www.lumindoind.com
        </li>
      </ul>
      <address class="address">
        418 W. Cedar Avenue<br>
        Suite 200, Tempe
      </address>
    </div>
  </section>
</body>
</html>
```